Upmarket Bathroom and Kitchen ware supplier needs a classy business card design

We are a company based in Fiji, we sell plumbing ware (Kitchen and bathroom taps, Basins,showers, toilets etc) through up market show rooms to individuals and directly through Architects and designers of resorts and holiday houses for new builds and renovations. we are wanting to upgrade our over all look and brand. we are starting with a new logo but will be rebranding the whole business. This project is for a business card design for my management and tales team I would like it to be dark, classy and interesting

Target Market(s)

Resort directors and Management, High end holiday home owners

Contact Information for Business Card

Neil Dawson
Director
+64219473815

Colors

Designer to choose colors to be used in the design.

Requirements
Must have
• Must have an upmarket appearance I like darker charcoal shades but will be guided by the designers
• Please any catch phrases like "Crafting remarkable living rooms" this belongs tpo one of our suppliers so can not be used.
Nice to have
• Double sided, so front dedicated to logo provided and back info about the business and the person.

```html
<!DOCTYPE html>
<html lang="en">
<head>
<meta charset="utf-8">
<title>Coralview Interiors – Business Card</title>
<link rel="stylesheet" href="https://fonts.googleapis.com/css2?family=Heebo:wght@300;400&family=Josefin+Sans:wght@300&family=Roboto+Condensed:wght@300&display=swap">
<style>
  :root {
    --backdrop: #9a9a9a;
    --charcoal: #222222;
    --signal-red: #ed1c24;
    --paper-white: #ffffff;
  }
  * { margin: 0; padding: 0; box-sizing: border-box; }
  html, body {
    width: 1200px;
    height: 1200px;
    overflow: hidden;
    background: var(--backdrop);
  }
  .canvas {
    position: relative;
    width: 1200px;
    height: 1200px;
  }
  .card {
    position: absolute;
    left: 181px;
    width: 839px;
    height: 482px;
    background: var(--charcoal);
    overflow: hidden;
  }
  .card--front { top: 115px; }
  .card--back { top: 637px; }

  .brand__dot {
    position: absolute;
    border: 1.5px solid var(--signal-red);
    border-radius: 50%;
  }
  .brand__lockup {
    position: absolute;
    display: flex;
    flex-direction: column;
    align-items: center;
    color: var(--signal-red);
    font-family: "Josefin Sans", sans-serif;
    font-weight: 300;
    text-transform: uppercase;
    white-space: nowrap;
    line-height: 1;
  }
  .brand__rule {
    height: 1px;
    background: var(--paper-white);
  }

  /* front lockup */
  .card--front .brand__dot { left: 196px; top: 170px; width: 96px; height: 96px; border-width: 2px; }
  .card--front .brand__lockup { left: 342px; top: 206px; width: 300px; }
  .card--front .brand__word { font-size: 36px; letter-spacing: 0.3em; padding-left: 0.3em; }
  .card--front .brand__rule { width: 236px; margin-top: 12px; }
  .card--front .brand__sub { font-size: 13px; letter-spacing: 0.9em; padding-left: 0.9em; margin-top: 12px; }

  /* back lockup */
  .card--back .brand__dot { left: 540px; top: 362px; width: 52px; height: 52px; }
  .card--back .brand__lockup { left: 617px; top: 372px; width: 160px; }
  .card--back .brand__word { font-size: 18px; letter-spacing: 0.3em; padding-left: 0.3em; }
  .card--back .brand__rule { width: 118px; margin-top: 6px; }
  .card--back .brand__sub { font-size: 8px; letter-spacing: 0.6em; padding-left: 0.6em; margin-top: 6px; }

  .contact {
    position: absolute;
    right: 496px;
    top: 178px;
    text-align: right;
  }
  .contact__name {
    color: var(--signal-red);
    font-family: "Heebo", sans-serif;
    font-weight: 300;
    font-size: 40px;
    line-height: 1;
    word-spacing: 0.2em;
  }
  .contact__role,
  .contact__label {
    color: var(--paper-white);
    font-family: "Heebo", sans-serif;
    font-weight: 300;
    font-size: 17px;
    line-height: 1;
  }
  .contact__role { margin-top: 10px; }
  .contact__phone {
    margin-top: 18px;
    color: var(--signal-red);
    font-family: "Roboto Condensed", sans-serif;
    font-weight: 300;
    font-size: 33px;
    letter-spacing: 0.12em;
    line-height: 1;
    margin-right: -0.12em;
  }
  .contact__label { margin-top: 8px; }
</style>
</head>
<body>
<main class="canvas">
  <section class="card card--front" aria-label="Card front">
    <span class="brand__dot" aria-hidden="true"></span>
    <div class="brand__lockup">
      <span class="brand__word">Coralview</span>
      <span class="brand__rule" aria-hidden="true"></span>
      <span class="brand__sub">Interiors</span>
    </div>
  </section>

  <section class="card card--back" aria-label="Card back">
    <div class="contact">
      <p class="contact__name">Neil Dawson</p>
      <p class="contact__role">Director</p>
      <p class="contact__phone">+64219473815</p>
      <p class="contact__label">Contact</p>
    </div>
    <span class="brand__dot" aria-hidden="true"></span>
    <div class="brand__lockup">
      <span class="brand__word">Coralview</span>
      <span class="brand__rule" aria-hidden="true"></span>
      <span class="brand__sub">Interiors</span>
    </div>
  </section>
</main>
</body>
</html>
```